Business card design for web travel company

Hi
we'd like to receive some proposal for a business card design.
Stayvano is a private travel club, dedicated to all travel lovers, with unique offers for exclusive destinations all around the world. At Stayvano you can find a wide range of offers for resorts, boutique hotels and travel packages at the best guaranteed price available on the market. The convenience of the offer is guaranteed by a private sales model: offers are available for a limited time only and they are personally chosen by Stayvano's qualified team of travel experts.
We offer only exclusive hotels with discounted prices but we are not an outlet or a discount supermarket: the design should reflect our connection with luxury, exclusivity using the same style of our website www.stayvano-example.com.
We want to make sure that when we'll present ourself to our business partner they will feel immediately which is our brand positioning giving them also a sense of an affordable and reliable partner.
In attachment you can also find our brand guidelines (please note that we are NOT USING ANY MORE THE TAG LINE "Five star outlet" mentioned in it).
The info to be inserted are:
Name Surname
Job Title
Tel
Mobile (when needed)
Email
Stayvano S.r.l.
Via Bruno Lesta 27
20131 Milano

```html
<!DOCTYPE html>
<html lang="en">
<head>
<meta charset="utf-8">
<title>Stayvano – Business Card</title>
<link rel="stylesheet" href="https://fonts.googleapis.com/css2?family=Exo+2:wght@300&family=Arimo:wght@400;700&display=swap">
<style>
  :root {
    --page: #ffffff;
    --band: #231f20;
    --gold: #c9b98a;
    --gold-light: #f1e9cf;
    --ink: #1a1a1a;
    --ink-soft: #555555;
    --logo-dark: #2b2b2b;
    --sky: #7fb0df;
    --sea: #1f5f9e;
    --sea-deep: #154a86;
  }
  html, body {
    margin: 0;
    padding: 0;
    width: 1010px;
    height: 1200px;
    overflow: hidden;
    background: var(--page);
  }
  .canvas {
    position: relative;
    width: 1010px;
    height: 1200px;
  }
  .card {
    position: absolute;
    left: 24px;
    width: 966px;
    height: 546px;
    overflow: hidden;
    box-shadow: 10px 12px 18px rgba(0,0,0,0.28);
  }
  /* Front */
  .card-front {
    top: 20px;
    background: linear-gradient(180deg, #ffffff 0%, #ffffff 60%, #f3f3f3 100%);
  }
  .brand-band {
    position: absolute;
    left: 0; top: 0;
    width: 100%;
    height: 158px;
    background: var(--band);
  }
  .brand-rule {
    position: absolute;
    left: 0; top: 158px;
    width: 100%;
    height: 14px;
    background: linear-gradient(90deg, var(--band) 0%, var(--gold) 30%, var(--gold-light) 55%, var(--gold) 80%, var(--band) 100%);
  }
  .brand-shade {
    position: absolute;
    left: 0; top: 172px;
    width: 100%;
    height: 40px;
    background: linear-gradient(180deg, rgba(0,0,0,0.12), rgba(0,0,0,0));
  }
  .wordmark {
    position: absolute;
    margin: 0;
    font-family: "Exo 2", sans-serif;
    font-weight: 300;
    letter-spacing: 1px;
    line-height: 1;
  }
  .card-front .wordmark {
    left: 46px;
    top: 40px;
    font-size: 82px;
    color: #ffffff;
  }
  .holder-name {
    position: absolute;
    left: 46px;
    top: 268px;
    margin: 0;
    font-family: "Exo 2", sans-serif;
    font-weight: 300;
    font-size: 36px;
    line-height: 1.2;
    color: var(--ink);
  }
  .job-title {
    position: absolute;
    left: 46px;
    top: 320px;
    margin: 0;
    font-family: "Arimo", sans-serif;
    font-size: 22px;
    color: var(--ink-soft);
  }
  .contact,
  .company-address {
    position: absolute;
    margin: 0;
    font-family: "Arimo", sans-serif;
    font-size: 25px;
    line-height: 37px;
    color: var(--ink);
    font-style: normal;
  }
  .contact {
    left: 46px;
    top: 436px;
  }
  .company-address {
    right: 46px;
    top: 399px;
    text-align: right;
  }
  .contact b,
  .company-address b { font-weight: 700; }
  /* Back */
  .card-back {
    top: 622px;
  }
  .scene {
    position: absolute;
    inset: 0;
    background: linear-gradient(180deg, var(--sky) 0%, #9cc3e6 32%, var(--sea) 42%, var(--sea-deep) 100%);
  }
  .card-back .wordmark {
    left: 46px;
    top: 34px;
    font-size: 96px;
    color: var(--logo-dark);
  }
  .web-address {
    position: absolute;
    left: 50px;
    top: 146px;
    margin: 0;
    font-family: "Arimo", sans-serif;
    font-size: 28px;
    color: var(--ink);
  }
</style>
</head>
<body>
  <main class="canvas">
    <section class="card card-front">
      <div class="brand-band"></div>
      <div class="brand-rule"></div>
      <div class="brand-shade"></div>
      <h1 class="wordmark">Stayvano</h1>
      <p class="holder-name">Marco Rinaldi</p>
      <p class="job-title">Partnership Manager</p>
      <p class="contact">
        <b>Tel:</b> 555 014 2288<br>
        <b>E-mail:</b> mrinaldi@stayvano-example.com
      </p>
      <address class="company-address">
        <b>Stayvano S.r.l.</b><br>
        Via Bruno Lesta 27<br>
        20131 Milano
      </address>
    </section>

    <section class="card card-back">
      <div class="scene" role="img" aria-label="Travel photograph of a seaside terrace overlooking the sea under a clear sky"></div>
      <h2 class="wordmark">Stayvano</h2>
      <p class="web-address">www.stayvano-example.com</p>
    </section>
  </main>
</body>
</html>
```